Fresh and unique Mortgage Broking business needs website design.

We need a professional yet fresh, bright and colourful website for my Mortgage broking business.
We specialise in the Non conforming/sub prime market with clients who have been rejected by other banks or have trouble getting finance through a traditional lender.
We are called Lark Lending and we aim to provide Hope to our clients when they have thought there was no hope.
I would like it to be on a Wordpress platform as I plan to do a lot of postings, both written and video and I need it to be easy to use.
I would also like it to be able to have a clear and simple enquiry box on the first page to capture contact details and notify me via email.

I have already had the logo designed in both green and black and a white version.
I have also had a a header made up using the white logo with leaves background that could possibly be used as the website header which I have used as my facebook header.

https://www.facebook.com/MarcusWendellLark/

I tried playing around with a jimdo website builder which kind of got some of the brightness and colours I was after but it had a lot to go.

http://larklending.sitebuildr.example/

Colors
0292cd
00a990
fbed22
ffc214
f78f20
ec1f27

• I'm not sure what the difference between uncoded and coded website is so I'm not sure what I need?

```html
<!DOCTYPE html>
<html lang="en">
<head>
<meta charset="utf-8">
<title>Lark Lending</title>
<link rel="stylesheet" href="https://fonts.googleapis.com/css2?family=Jost:wght@400;500&family=Open+Sans:wght@400;600&display=swap">
<style>
:root{
  --teal:#0a9c86;
  --teal-dark:#087e6c;
  --blue:#1a8cc6;
  --blue-band:#1b7fb8;
  --ink:#333;
  --muted:#6b6b6b;
  --grey-band:#f2f2f2;
  --line:#d9d9d9;
  --brand-green:#1f6b3a;
  --white:#fff;
}
*{box-sizing:border-box;margin:0;padding:0}
html,body{width:1200px;height:2525px;overflow:hidden;background:var(--white)}
body{font-family:"Open Sans",Arial,sans-serif;color:var(--ink);position:relative}
.heading{font-family:"Jost",Arial,sans-serif;font-weight:400;text-transform:uppercase;letter-spacing:.5px}
section,header,footer{position:absolute;left:0;width:1200px}

/* header */
.site-header{top:0;height:122px;background:var(--white)}
.brand{position:absolute;left:100px;top:30px;display:flex;align-items:center;gap:10px}
.brand-dot{width:18px;height:18px;border-radius:50%;background:var(--brand-green)}
.brand-name{font-family:"Open Sans",Arial,sans-serif;font-weight:600;font-size:28px;color:var(--brand-green)}
.contact-bar{position:absolute;right:88px;top:28px;display:flex;align-items:center;gap:6px;font-size:19px;color:#222}
.contact-bar .socials{display:flex;gap:7px;margin-left:16px}
.contact-bar .socials span{width:19px;height:19px;border-radius:3px;background:var(--blue)}
.main-nav{position:absolute;right:84px;top:74px;display:flex;gap:10px}
.main-nav a{font-size:16px;color:#222;text-decoration:none;padding:6px 20px;border-radius:18px}
.main-nav a.active{color:var(--teal);border:1px solid #d6d6d6;box-shadow:0 0 4px rgba(0,0,0,.12)}

/* hero */
.hero{top:122px;height:521px}
.hero-photo{position:absolute;inset:0;background:linear-gradient(90deg,#f0f0f0 0%,#ececec 45%,#e4e4e4 60%,#d8d8d8 80%,#e9e9e9 100%)}
.hero-text{position:absolute;left:92px;top:200px}
.hero-title{font-family:"Open Sans",Arial,sans-serif;font-weight:600;font-size:48px;color:var(--teal);letter-spacing:.5px}
.hero-sub{font-size:17px;font-weight:600;color:#222;line-height:25px;margin-top:10px;width:380px}
.hero-arrows{display:flex;gap:6px;margin-top:28px}
.hero-arrows span{width:26px;height:26px;border-radius:50%;background:#555;display:flex;align-items:center;justify-content:center}

/* about */
.about{top:643px;height:373px}
.about-photo{position:absolute;left:96px;top:60px;width:258px;height:258px;border-radius:50%;background:radial-gradient(circle at 50% 40%,#c9a083 0%,#9a7158 35%,#3a3f4a 70%,#e9e9e9 71%);border:4px solid #eee}
.about-body{position:absolute;left:387px;top:67px;width:703px}
.section-title{font-size:28px;color:var(--blue)}
.copy{font-size:14px;line-height:27px;color:#444;text-align:justify;margin-top:10px}
.btn-outline{display:inline-block;margin-top:24px;font-size:13px;color:var(--teal);border:1px solid var(--teal);border-radius:20px;padding:9px 20px;box-shadow:0 1px 3px rgba(0,0,0,.15)}

/* services */
.services{top:1016px;height:468px;background:var(--grey-band);text-align:center}
.services .section-title{margin-top:58px;font-size:31px}
.services .tagline{font-size:20px;color:#555;margin-top:4px}
.service-list{display:flex;position:absolute;left:92px;top:166px;width:1024px;justify-content:space-between}
.service{width:230px}
.service-icon{width:94px;height:94px;border-radius:50%;background:var(--teal);margin:0 auto;display:flex;align-items:center;justify-content:center}
.service-name{font-size:16px;font-weight:400;color:#222;margin-top:22px;text-transform:uppercase}
.service-text{font-size:12px;line-height:18px;color:var(--muted);margin:14px auto 0;width:200px;text-align:justify;text-align-last:center}
.read-link{display:block;font-size:12px;color:var(--blue);margin-top:14px}

/* love */
.love{top:1484px;height:409px}
.love-photo{position:absolute;left:92px;top:56px;width:486px;height:275px;border:6px solid var(--white);box-shadow:0 0 6px rgba(0,0,0,.35);background:linear-gradient(180deg,#5f8a3f 0%,#a9c27a 35%,#e8e1d2 55%,#6e9e42 100%)}
.love-body{position:absolute;left:611px;top:74px;width:500px}
.love-body .copy{font-size:13.5px;line-height:26px}

/* blog */
.blog{top:1893px;height:312px;background:linear-gradient(180deg,#1e86bd 0%,#1576b0 100%);color:var(--white)}
.blog .heading{text-align:center;font-size:28px;margin-top:50px}
.post{position:absolute;top:122px;display:flex;gap:18px;width:490px}
.post-thumb{width:163px;height:143px;border:2px solid #d9e6ef;flex:none}
.post h3{font-size:15px;font-weight:600;margin-top:8px}
.post .date{font-size:12px;margin-top:10px}
.post p{font-size:11px;line-height:20px;margin-top:6px;text-align:justify}
.post .more{font-size:12px;margin-top:4px;display:block}

/* footer */
.site-footer{top:2205px;height:320px}
.footer-brand{position:absolute;left:92px;top:96px;display:flex;align-items:center;gap:10px}
.footer-col{position:absolute;top:70px}
.footer-col h4{font-size:14px;font-weight:400;color:#222;text-transform:uppercase}
.footer-col p{font-size:11.5px;line-height:22px;color:#666;margin-top:16px}
.signup{display:flex;margin-top:14px}
.signup span{width:150px;height:31px;border:1px solid #ccc;font-size:11px;color:#555;padding:8px 8px}
.signup b{width:57px;height:31px;background:var(--teal);color:var(--white);font-size:12px;font-weight:400;text-align:center;line-height:31px}
.footer-socials{display:flex;gap:12px;margin-top:26px}
.footer-socials span{width:25px;height:25px;border-radius:4px;background:#444}
.footer-rule{position:absolute;left:92px;right:88px;top:258px;border-top:1px solid var(--line)}
.copyright{position:absolute;top:282px;width:100%;text-align:center;font-size:12px;color:#333}
</style>
</head>
<body>

<header class="site-header">
  <div class="brand"><span class="brand-dot"></span><span class="brand-name">Lark Lending</span></div>
  <div class="contact-bar">
    <svg width="18" height="18" viewBox="0 0 18 18"><rect width="18" height="18" rx="3" fill="#1a8cc6"/><path d="M5 4l2 0 1 3-1.3 1c.7 1.4 1.8 2.5 3.2 3.2l1-1.3 3 1v2c0 .6-.5 1-1 1C8 14 4 10 4 5c0-.5.4-1 1-1z" fill="#fff"/></svg>
    <span>0400 318 562</span>
    <div class="socials" aria-label="Social links"><span></span><span></span><span></span><span style="background:#d9342b"></span></div>
  </div>
  <nav class="main-nav">
    <a class="active">HOME</a><a>ABOUT</a><a>SERVICES</a><a>PROPERTY ADVICE</a><a>CONTACT</a>
  </nav>
</header>

<section class="hero">
  <div class="hero-photo" role="img" aria-label="Photo of a woman working at a white desk in a bright minimal room"></div>
  <div class="hero-text">
    <h1 class="hero-title">LARK LENDING</h1>
    <p class="hero-sub">We aim to provide a way forward to our clients when they have thought there was no hope</p>
    <div class="hero-arrows">
      <span><svg width="10" height="10" viewBox="0 0 10 10"><path d="M6.5 1.5L3 5l3.5 3.5" stroke="#fff" stroke-width="2" fill="none"/></svg></span>
      <span><svg width="10" height="10" viewBox="0 0 10 10"><path d="M3.5 1.5L7 5 3.5 8.5" stroke="#fff" stroke-width="2" fill="none"/></svg></span>
    </div>
  </div>
</section>

<section class="about">
  <div class="about-photo" role="img" aria-label="Portrait photo of Marcus, the broker"></div>
  <div class="about-body">
    <h2 class="section-title heading">About Us</h2>
    <p class="copy">Marcus lives in Fernbrook and loves exploring the Ashvale Shire with his wife and kids for great places to eat. With over 10 years' experience in financial services ranging from insurance, superannuation, investments and finance, Marcus bringing together his experience to provide a more holistic approach to his customers. Marcus has a Diploma in Financial Planning, a Certificate IV in Finance and Mortgage Broking, and is a member of the NLBA Marcus is a real family man who loves spending time with his wife and kids. What he finds most rewarding is being able to help people in difficult situations</p>
    <span class="btn-outline">Read More &raquo;</span>
  </div>
</section>

<section class="services">
  <h2 class="section-title heading">Our Service</h2>
  <p class="tagline">Neque porro quisquam est qui dolorem</p>
  <div class="service-list">
    <div class="service">
      <div class="service-icon"><svg width="28" height="36" viewBox="0 0 28 36"><rect x="2" y="2" width="24" height="32" fill="#fff"/><g fill="#0a9c86"><rect x="6" y="6" width="4" height="4"/><rect x="12" y="6" width="4" height="4"/><rect x="18" y="6" width="4" height="4"/><rect x="6" y="13" width="4" height="4"/><rect x="12" y="13" width="4" height="4"/><rect x="18" y="13" width="4" height="4"/><rect x="6" y="20" width="4" height="4"/><rect x="18" y="20" width="4" height="4"/><rect x="11" y="26" width="6" height="8"/></g></svg></div>
      <h3 class="service-name">Residential Loans</h3>
      <p class="service-text">Helping employers launch new programs that enhance health and advance organization</p>
      <span class="read-link">Read More &raquo;</span>
    </div>
    <div class="service">
      <div class="service-icon"><svg width="42" height="26" viewBox="0 0 42 26"><rect x="1" y="1" width="40" height="24" fill="#fff"/><rect x="5" y="5" width="32" height="16" fill="none" stroke="#0a9c86" stroke-width="2"/><circle cx="21" cy="13" r="5" fill="#0a9c86"/></svg></div>
      <h3 class="service-name">Investment Loans</h3>
      <p class="service-text">Helping providers improve the scientific validity and effective implementation of their</p>
      <span class="read-link">Read More &raquo;</span>
    </div>
    <div class="service">
      <div class="service-icon"><svg width="40" height="30" viewBox="0 0 40 30" fill="#fff"><circle cx="20" cy="8" r="6"/><path d="M10 28c0-7 4-11 10-11s10 4 10 11z"/><circle cx="8" cy="11" r="4"/><path d="M1 26c0-5 3-8 7-8 1.5 0 2.5.3 3.5 1-1.5 2-2.5 4.5-2.5 7z"/><circle cx="32" cy="11" r="4"/><path d="M39 26c0-5-3-8-7-8-1.5 0-2.5.3-3.5 1 1.5 2 2.5 4.5 2.5 7z"/></svg></div>
      <h3 class="service-name">Self Employed Loans</h3>
      <p class="service-text">Helping hospitals integrate health promotion concepts into patient care, staff and employee</p>
      <span class="read-link">Read More &raquo;</span>
    </div>
    <div class="service">
      <div class="service-icon"><svg width="28" height="34" viewBox="0 0 28 34"><path d="M2 1h17l8 8v24H2z" fill="#fff"/><path d="M19 1v8h8" fill="#cfe9e4"/><g stroke="#0a9c86" stroke-width="2"><path d="M7 15h14M7 20h14M7 25h14"/></g></svg></div>
      <h3 class="service-name">Non Confirming Loans</h3>
      <p class="service-text">Forming international collaborations that advance policy and practice and stimulate</p>
      <span class="read-link">Read More &raquo;</span>
    </div>
  </div>
</section>

<section class="love">
  <div class="love-photo" role="img" aria-label="Photo of a smiling family of four outside their house"></div>
  <div class="love-body">
    <h2 class="section-title heading">We Love What We Do</h2>
    <p class="copy">Marcus lives in Fernbrook and loves exploring the Ashvale Shire with his wife and kids for great places to eat. With over 10 years' experience in financial services ranging from insurance, superannuation, investments and finance, Marcus bringing together his experience to provide a more holistic approach to his customers. Marcus has a Diploma in Financial Planning, a Certificate IV in Finance and Mortgage Broking, and is a member of the NLBA Marcus is a real family man who loves spending time with his wife and kids. What he finds most rewarding is being able</p>
    <span class="btn-outline">Read More &raquo;</span>
  </div>
</section>

<section class="blog">
  <h2 class="heading">Latest Blog</h2>
  <article class="post" style="left:92px">
    <div class="post-thumb" role="img" aria-label="Photo of a laptop on a desk" style="background:linear-gradient(135deg,#3a2a22,#c9a27a 60%,#efe3d3)"></div>
    <div>
      <h3>Nemo Enim Ipsam Volup</h3>
      <p class="date">09-07-2016</p>
      <p>Lorem Ipsum has been the industry's standard dummy text ever since the 1500s, when an unknown printer took a galley of type and scrambled it to make a type specimen</p>
      <span class="more">Read More &gt;&gt;</span>
    </div>
  </article>
  <article class="post" style="left:631px;top:114px">
    <div class="post-thumb" role="img" aria-label="Photo of a person packing moving boxes" style="background:linear-gradient(135deg,#6b5a4c,#b59a7c 55%,#d8cfc4)"></div>
    <div>
      <h3>Nemo Enim Ipsam Volup</h3>
      <p class="date">09-07-2016</p>
      <p>Lorem Ipsum has been the industry's standard dummy text ever since the 1500s, when an unknown printer took a galley of type and scrambled it to make a type specimen</p>
      <span class="more">Read More &gt;&gt;</span>
    </div>
  </article>
</section>

<footer class="site-footer">
  <div class="footer-brand"><span class="brand-dot"></span><span class="brand-name">Lark Lending</span></div>
  <div class="footer-col" style="left:374px">
    <h4>Contact Us</h4>
    <p>Address : 12 Larkspur Lane, Westvale<br>WV4 2KT<br>Phone : +61 3 5550 1842<br>Email : info@larklending.example</p>
  </div>
  <div class="footer-col" style="left:647px">
    <h4>Join Our Mailing List</h4>
    <p style="width:210px;line-height:18px">Your about us information would fit here nicely.</p>
    <div class="signup"><span>Email address</span><b>Submit</b></div>
  </div>
  <div class="footer-col" style="left:937px">
    <h4>Follow Us Out There</h4>
    <div class="footer-socials" aria-label="Social links"><span></span><span></span><span></span><span></span></div>
  </div>
  <div class="footer-rule"></div>
  <p class="copyright">Copyright &copy; 2016. All Rights Reserved</p>
</footer>

</body>
</html>
```